Logo and label design for our product coffee scrub

We need a logo design and a packaging label design for our new brand called "Freddy Velvetoni". Best design wins 500$

It's a cosmetic brand with initial product "coffee scrub", which is a body peeling made of coffee, himalayan salt and additives. Brand will target young to middle aged women, who we will address with a very sexy and slightly provocative appeal (pictures of women wearing nothing but our coffee scrub - sample attached). Purpose of the coffee scrub is to target cellulite, stretch marks, psoriasis, varicose veins, eczema and acne.

Packaging that we will use will be a brown stand up pouch (attached) with a dimensions width 13cm, height 22cm and with a front and back sticker (dimensions width 7cm, height 14cm, round corners) or sticker that overlaps from front to back.

Looking forward on receiving your ideas!

Target Market(s)

Brand will targeting young to middle aged european women, who we will address with a very sexy and slightly provocative appeal (pictures of women wearing nothing but our coffee scrub - sample attached)

Industry/Entity Type

Product

Requirements
Must have
• Just an idea for the logo writing to use a handwriting font "Freddy Velvetoni".

For the front side of packaging label you could use a picture of a women's body wearing a coffee scrub. Label should be very sexy but not vulgar.
Nice to have
• The back side of the label should have a cheesy pick up line and declaration text (just a sample):

hi babe! so you wanna get dirty! just show me the way to your bath. but first let me give you a proper introduction of myself. my name is freddy and i'm a coffee scrub wearing nothing but 250g of finest arabic coffee and sweet orange flavour & lots of other good stuff.

by the way I will help you with cellulite, stretch marks, psoriasis, varicose veins, eczema and acne. i’ll smooth your lumps and bumps with brown sugar & sea salt, moisturise and tone your skin with cold pressed sweet almond oil, and use vitamins & minerals to work wonders from the outside in. then i’ll make us both smell good with a little orange essence.

ingredients:
Coffea Robusta Seed Powder (Coffee), Prunus Amygdalus Dulcis (Sweet Almond) Oil, Water (Aqua), Sodium Chloride (Salt), Sucrose (Brown Sugar). All ingredients organic.

net weight: 200 g

best before date:

barcode

```html
<!DOCTYPE html>
<html lang="en">
<head>
<meta charset="utf-8">
<title>Freddy Velvetoni – Coffee Scrub Labels</title>
<link rel="stylesheet" href="https://fonts.googleapis.com/css2?family=Josefin+Sans:wght@400;600&family=Nothing+You+Could+Do&family=Oswald:wght@500&family=Pompiere&family=Raleway:wght@400&display=swap">
<style>
  :root {
    --canvas-bg: #ececec;
    --label-black: #1c1b1c;
    --accent-orange: #ea5a1c;
    --stripe-grey: #d3d3cd;
    --stripe-shadow: #9c9c96;
    --text-white: #f4f4f2;
    --tagline-grey: #b9b9b4;
    --photo-light: #d9d7d3;
    --photo-skin: #9a5a35;
  }
  * { margin: 0; padding: 0; box-sizing: border-box; }
  html, body {
    width: 1200px; height: 775px; overflow: hidden;
    background: var(--canvas-bg);
  }
  .canvas {
    position: relative; width: 1200px; height: 775px;
    background: radial-gradient(ellipse at center, #f7f7f7 0%, var(--canvas-bg) 75%);
  }
  .label {
    position: absolute; top: 67px;
    width: 320px; height: 640px;
    background: var(--label-black);
    border-radius: 16px;
    overflow: hidden;
    box-shadow: 0 6px 18px rgba(0,0,0,0.18);
  }
  .label--front { left: 250px; }
  .label--back { left: 630px; }
  .label__stripes {
    position: absolute; left: 0; top: 0;
    width: 80px; height: 640px;
  }

  /* front */
  .brand {
    position: absolute; top: 52px; left: 70px;
    display: flex; align-items: center; gap: 10px;
  }
  .brand__dot {
    width: 30px; height: 30px; border-radius: 50%;
    border: 2px solid var(--text-white);
  }
  .brand__name {
    font-family: "Raleway", sans-serif; font-weight: 400;
    font-size: 15px; letter-spacing: 0.3px; color: var(--text-white);
    text-transform: uppercase;
  }
  .product-box {
    position: absolute; top: 120px; left: 102px;
    width: 120px; height: 64px;
    border: 3px solid var(--accent-orange);
    display: flex; flex-direction: column; justify-content: center; align-items: center;
    font-family: "Josefin Sans", sans-serif; font-weight: 600;
    font-size: 20px; line-height: 1.05; letter-spacing: 3px;
    color: var(--accent-orange); padding-top: 4px;
  }
  .tagline {
    position: absolute; top: 196px; left: 112px;
    font-family: "Nothing You Could Do", cursive;
    font-size: 17px; color: var(--tagline-grey);
  }
  .front-rule {
    position: absolute; top: 245px; left: 0; width: 100%; height: 5px;
    background: var(--accent-orange);
  }
  .front-photo {
    position: absolute; top: 254px; left: 46px; right: 9px; bottom: 18px;
    background:
      radial-gradient(ellipse 60% 55% at 45% 95%, var(--photo-skin) 0%, rgba(154,90,53,0) 100%),
      linear-gradient(160deg, #ecebe8 0%, var(--photo-light) 60%, #b8aaa0 100%);
  }

  /* back */
  .back-copy {
    position: absolute; top: 0; left: 0; width: 100%; height: 100%;
    color: var(--text-white);
  }
  .back-heading {
    position: absolute;
    font-family: "Pompiere", sans-serif; font-size: 22px;
    color: var(--accent-orange); text-transform: lowercase; line-height: 1;
  }
  .back-text {
    position: absolute;
    font-family: "Oswald", sans-serif; font-weight: 500;
    font-size: 10.4px; line-height: 1.62; letter-spacing: 0.15px;
  }
  .greeting { top: 24px; left: 20px; }
  .intro { top: 50px; left: 20px; width: 285px; }
  .benefits { top: 160px; left: 74px; width: 232px; }
  .ingredients-heading { top: 312px; left: 42px; }
  .ingredients { top: 338px; left: 42px; width: 262px; }
  .net-weight { top: 430px; left: 42px; }
  .best-before {
    top: 474px; left: 42px;
    display: flex; align-items: center; gap: 6px;
  }
  .best-before__field {
    display: inline-block; width: 86px; height: 24px;
    background: #ffffff;
  }
</style>
</head>
<body>
<main class="canvas">

  <section class="label label--front" aria-label="Front label">
    <svg class="label__stripes" viewBox="0 0 80 640" role="img" aria-label="Hand-painted black and white stripe border">
      <defs>
        <linearGradient id="stripeFront" x1="0" y1="0" x2="1" y2="0">
          <stop offset="0" stop-color="var(--stripe-grey)"/>
          <stop offset="1" stop-color="var(--stripe-shadow)"/>
        </linearGradient>
      </defs>
      <path d="M0 0 H30 C26 60 34 120 30 180 C28 240 40 300 44 360 C48 420 40 470 38 520 C36 570 40 610 36 640 H0 Z" fill="url(#stripeFront)"/>
    </svg>

    <div class="brand">
      <span class="brand__dot"></span>
      <span class="brand__name">Freddy Velvetoni</span>
    </div>

    <div class="product-box"><span>COFFEE</span><span>SCRUB</span></div>
    <p class="tagline">a body peeling</p>
    <div class="front-rule"></div>
    <div class="front-photo" role="img" aria-label="Photo of a woman wearing coffee scrub on her skin"></div>
  </section>

  <section class="label label--back" aria-label="Back label">
    <svg class="label__stripes" viewBox="0 0 80 640" role="img" aria-label="Hand-painted black and white stripe border">
      <defs>
        <linearGradient id="stripeBack" x1="0" y1="0" x2="1" y2="0">
          <stop offset="0" stop-color="var(--stripe-grey)"/>
          <stop offset="1" stop-color="var(--stripe-shadow)"/>
        </linearGradient>
      </defs>
      <path d="M0 0 H14 C12 50 20 100 34 150 C50 200 62 250 60 300 C58 350 40 390 30 420 C22 460 24 520 20 580 C18 610 20 630 18 640 H0 Z" fill="url(#stripeBack)"/>
    </svg>

    <div class="back-copy">
      <h2 class="back-heading greeting">hi babe!</h2>
      <p class="back-text intro">so you wanna get dirty! just show me the way to your bath. but first let me give you a proper introduction of myself. my name is freddy and i'm a coffee scrub wearing nothing but 250g of finest arabic coffee and sweet orange flavour &amp; lots of other good stuff.</p>
      <p class="back-text benefits">by the way I will help you with cellulite, stretch marks, psoriasis, varicose veins, eczema and acne. i'll smooth your lumps and bumps with brown sugar &amp; sea salt, moisturise and tone your skin with cold pressed sweet almond oil, and use vitamins &amp; minerals to work wonders from the outside in. then i'll make us both smell good with a little orange essence.</p>
      <h3 class="back-heading ingredients-heading">ingredients:</h3>
      <p class="back-text ingredients">Coffea Robusta Seed Powder (Coffee), Prunus Amygdalus Dulcis (Sweet Almond) Oil, Water (Aqua), Sodium Chloride (Salt), Sucrose (Brown Sugar).<br>All ingredients organic.</p>
      <p class="back-heading net-weight">net weight: 200 g</p>
      <p class="back-heading best-before">best before date: <span class="best-before__field"></span></p>
    </div>
  </section>

</main>
</body>
</html>
```